UK Leading HighTech Tooling distributor letterhead

We are one of the UK's leading Engineering Tooling distributers, we are launching our great new catalogue in May and want a red-hot eye catching letterhead to accompany the catalogue.

We want customers who see it to think high quality and premium.

We will roll out the successful style of design accross our other marketing goods (bus cards, website, emails etc) so the winning design will gain more work as a result.

Finally - we are in a rush so please submit quickly your best designs!

Target Market(s)

Precision engineers, senior buyers and managing directors.

Industry/Entity Type

Marketing

Requirements
Must have
• It must feature the Brandor logo as the MAIN logo.
It must have a tag line of 'Complete Tooling Solutions' somewhere on the page.
It should feature our 6 supplier logo's as sub logo's

Contact details:
tel 01632 960417
fax 01632 960418
web brandorkit.co.uk
email sales@brandor.example
address : Brandor Ltd, Marsh Offices, Fennick Street, Holmbridge, North Calder, HX7 4QD, United Kingdom
Company registration 5718346
Vat no. 871 2043 58
Nice to have
• Bring our logo alive

I have attached an old version of our letterhead so you can see details - please make it much better!

```html
<!DOCTYPE html>
<html lang="en">
<head>
<meta charset="utf-8">
<title>Brandor Ltd Letterhead</title>
<link rel="stylesheet" href="https://fonts.googleapis.com/css2?family=Archivo:wght@700;800&family=Alegreya:wght@400&display=swap">
<style>
  :root {
    --sky-light: #eaf4fc;
    --sky-mid: #8cc3ea;
    --sky-deep: #3b9bdb;
    --brand-blue: #1f7fc4;
    --ink: #111111;
    --paper: #ffffff;
  }
  html, body {
    margin: 0;
    padding: 0;
    overflow: hidden;
    background: var(--paper);
  }
  .letterhead {
    position: relative;
    width: 848px;
    height: 1200px;
    background: var(--paper);
    overflow: hidden;
  }
  .header-band {
    position: absolute;
    top: 0;
    left: 0;
    width: 848px;
    height: 180px;
  }
  .brand-mark {
    position: absolute;
    left: 58px;
    top: 112px;
    display: flex;
    align-items: center;
    gap: 7px;
  }
  .brand-dot {
    width: 12px;
    height: 12px;
    border-radius: 50%;
    background: var(--brand-blue);
  }
  .brand-name {
    font-family: "Archivo", Arial, sans-serif;
    font-weight: 800;
    font-size: 24px;
    line-height: 28px;
    letter-spacing: 0.5px;
    color: var(--brand-blue);
  }
  .tagline {
    position: absolute;
    left: 232px;
    top: 62px;
    margin: 0;
    font-family: "Archivo", Arial, sans-serif;
    font-weight: 800;
    font-size: 21px;
    line-height: 24px;
    letter-spacing: 0.3px;
    color: var(--ink);
  }
  .contact {
    position: absolute;
    left: 670px;
    top: 34px;
    margin: 0;
    font-family: "Alegreya", Georgia, serif;
    font-size: 11px;
    line-height: 14px;
    color: var(--paper);
  }
  .suppliers {
    position: absolute;
    left: 36px;
    right: 36px;
    top: 1090px;
    display: flex;
    justify-content: space-between;
    align-items: center;
    font-family: "Archivo", Arial, sans-serif;
    font-weight: 800;
    font-size: 20px;
    color: var(--ink);
  }
  .supplier {
    display: flex;
    align-items: center;
    gap: 6px;
  }
  .supplier-square {
    width: 14px;
    height: 14px;
    background: var(--ink);
  }
  .supplier-badge {
    width: 28px;
    height: 22px;
    border-radius: 4px;
    background: var(--sky-mid);
  }
  .supplier-circle {
    width: 14px;
    height: 14px;
    border-radius: 50%;
    background: var(--ink);
  }
  .company-details {
    position: absolute;
    left: 0;
    width: 848px;
    top: 1131px;
    margin: 0;
    text-align: center;
    font-family: "Alegreya", Georgia, serif;
    font-size: 11.5px;
    line-height: 17px;
    color: var(--ink);
  }
</style>
</head>
<body>
<main class="letterhead">
  <svg class="header-band" viewBox="0 0 848 180" aria-hidden="true">
    <defs>
      <linearGradient id="bandFade" x1="0" y1="0" x2="1" y2="0">
        <stop offset="0" stop-color="#eaf4fc"/>
        <stop offset="0.45" stop-color="#8cc3ea"/>
        <stop offset="1" stop-color="#3b9bdb"/>
      </linearGradient>
    </defs>
    <path d="M0 0 H848 V121 H212 C196 92 150 72 104 72 C60 72 22 86 0 104 Z" fill="url(#bandFade)"/>
  </svg>

  <div class="brand-mark">
    <span class="brand-dot"></span>
    <span class="brand-name">BRANDOR</span>
  </div>

  <h1 class="tagline">COMPLETE TOOLING SOLUTIONS</h1>

  <p class="contact">
    tel: (01632) 960 417<br>
    fax: (01632) 960 418<br>
    e-mail: sales@brandor.example<br>
    web: www.brandorkit.co.uk
  </p>

  <div class="suppliers">
    <span class="supplier"><span class="supplier-square"></span>Ardent Inc.</span>
    <span class="supplier"><span class="supplier-badge"></span></span>
    <span class="supplier">Veltrano</span>
    <span class="supplier">Korvik</span>
    <span class="supplier"><span class="supplier-circle"></span>Halden Inc.</span>
    <span class="supplier">Tressa</span>
  </div>

  <p class="company-details">
    Brandor Ltd, Marsh Offices, Fennick Street, Holmbridge, North Calder, HX7 4QD, United Kingdom<br>
    Company registration: 5718346 Vat no: 871 2043 58
  </p>
</main>
</body>
</html>
```